Can Design for Fun, Growing Health Food Brand

We are launching a brand new product, electrolyte seltzer drinks. We want the design to be clean/simple and slightly modern while staying true to our brand identity. Must say "Mineral Hydration" as the product descriptor, sub headline is "Carbonated electrolyte beverage with sea moss and real fruit juice". First flavors will be Watermelon Mint and Mango.

Target Market(s)

Women ages 30-50 who are interested in health wellness/trends

Industry/Entity Type

Health & Wellness

Font styles to use
Sans Serif

Requirements
Must have
• Tall, skinny can, current Bright Kelp Co Logo, use aluminum on can as element in design.
Nice to have
• Be fun, clean and modern. Would like to see the label less busy than our gels.
Should not have
• Avoid putting flavor on bottom 1/5 of can. No gradient color changes. Do not want really detailed or realistic fruit image, prefer drawings or similar.

```html
<!DOCTYPE html>
<html lang="en">
<head>
<meta charset="utf-8">
<title>Bright Kelp Co – Mineral Hydration – Watermelon Mint</title>
<link href="https://fonts.googleapis.com/css2?family=Lexend:wght@500;600;700&display=swap" rel="stylesheet">
<style>
  :root {
    --ink: #ffffff;
    --night: #170f38;
    --melon: #d65c66;
    --melon-soft: #e3998e;
    --art-tint: rgba(255, 255, 255, 0.2);
  }
  * { margin: 0; padding: 0; box-sizing: border-box; }
  html, body { width: 1200px; height: 2315px; overflow: hidden; }
  body {
    position: relative;
    background: var(--night);
    font-family: "Lexend", sans-serif;
    color: var(--ink);
  }
  .hero-band {
    position: absolute; left: 0; top: 0;
    width: 1200px; height: 1073px;
    background: var(--melon-soft);
  }
  .label {
    position: absolute;
    width: 534px; height: 1073px;
    background: var(--melon);
    text-align: center;
    overflow: hidden;
  }
  .hero-band .label { left: 333px; top: 0; }
  .label--display {
    left: 333px; top: 1157px;
    transform: scale(0.8);
    transform-origin: top center;
    border-radius: 6px;
  }
  .brand-mark {
    position: absolute; left: 205px; top: 196px;
    width: 125px; height: 125px;
    border: 5px solid var(--ink); border-radius: 50%;
  }
  .brand-name {
    position: absolute; left: 0; right: 0; top: 348px;
    font-weight: 600; font-size: 54px; line-height: 64px; letter-spacing: 0;
    white-space: nowrap;
  }
  .descriptor {
    position: absolute; left: 0; right: 0; top: 464px;
    font-weight: 700; font-size: 32px; letter-spacing: 1px; line-height: 36px;
    white-space: nowrap;
  }
  .subline {
    position: absolute; left: 0; right: 0; top: 518px;
    font-weight: 600; font-size: 20.5px; line-height: 29px;
  }
  .flavor-art {
    position: absolute; left: 130px; top: 604px;
    width: 274px; height: 190px;
    border-radius: 40px 120px 40px 80px;
    background: var(--art-tint);
  }
  .flavor-name {
    position: absolute; left: 0; right: 0; top: 826px;
    font-weight: 700; font-size: 41px; line-height: 52px; letter-spacing: 1px;
    white-space: nowrap;
  }
  .volume {
    position: absolute; left: 0; right: 0; top: 960px;
    font-weight: 600; font-size: 26px; line-height: 30px;
  }
</style>
</head>
<body>
  <section class="hero-band">
    <article class="label">
      <div class="brand-mark"></div>
      <h1 class="brand-name">BRIGHT KELP CO</h1>
      <p class="descriptor">MINERAL HYDRATION</p>
      <p class="subline">Carbonated electrolyte beverage<br>with sea moss and real fruit juice</p>
      <div class="flavor-art" role="img" aria-label="Line drawing of a watermelon slice with mint leaves"></div>
      <h2 class="flavor-name">WATERMELON<br>MINT</h2>
      <p class="volume">250ml</p>
    </article>
  </section>

  <article class="label label--display">
    <div class="brand-mark"></div>
    <p class="brand-name">BRIGHT KELP CO</p>
    <p class="descriptor">MINERAL HYDRATION</p>
    <p class="subline">Carbonated electrolyte beverage<br>with sea moss and real fruit juice</p>
    <div class="flavor-art" role="img" aria-label="Line drawing of a watermelon slice with mint leaves"></div>
    <p class="flavor-name">WATERMELON<br>MINT</p>
    <p class="volume">250ml</p>
  </article>
</body>
</html>
```